Introducing a Personal Care Product called" ORBA"

We are a nutra-pharmaceutical company launching a new personal care product called ORBA. Some of the products include massage and aroma therapy, as well as personal lubricants. The products will be produced and put into, two bottles that are interlocking so two combinations of products can be purchased at once (i.e. massage and aroma therapy). The poster will be used for promotional advertising, trade shows and for in-store promotions.
Updates

We would like to see a design without the product.

Target Market(s)

Products will be aimed at adults primarily women 18-65 in the USA. We want to appeal to the everyday woman who is interested in their sexual well being.

Industry/Entity Type

Massage

Requirements
Must have
• Clean Presentation. Not many colors. Text should be as follows: ORBA for Her....ORBA for Him...ORBA for You...Let's ORBA see attached..Also ORBA with Her...Orba with Him..Let's ORBA..Open to other copy versions.
Nice to have
• Product image not necessary but can be used. image attached
Should not have
• Too many colors...

```html
<!DOCTYPE html>
<html lang="en">
<head>
<meta charset="utf-8">
<title>Let's ORBA — Poster</title>
<link rel="stylesheet" href="https://fonts.googleapis.com/css2?family=EB+Garamond:wght@400&display=swap">
<style>
  :root {
    --paper: #ffffff;
    --ink: #3a3a3a;
    --her-tone: #f2b8d0;
    --her-deep: #b02a4a;
    --him-tone: #bfe6f5;
    --him-deep: #2a5fc9;
    --clear: #eef1f4;
  }
  * { margin: 0; padding: 0; box-sizing: border-box; }
  html, body {
    width: 800px;
    height: 1200px;
    overflow: hidden;
    background: var(--paper);
  }
  .poster {
    position: relative;
    width: 800px;
    height: 1200px;
    background: var(--paper);
    font-family: "EB Garamond", "Times New Roman", serif;
    color: var(--ink);
  }
  .tagline {
    position: absolute;
    font-size: 48px;
    font-weight: 400;
    line-height: 1;
    white-space: nowrap;
  }
  .tagline--her { left: 44px; top: 18px; }
  .tagline--him { right: 44px; top: 52px; }
  .tagline--you {
    left: 0; right: 0; top: 1012px;
    text-align: center;
  }
  .product-pair {
    position: absolute;
    left: 52px;
    top: 110px;
    width: 696px;
    height: 900px;
    display: flex;
    gap: 6px;
  }
  .product-pair__bottle {
    flex: 1;
    border-radius: 26px 26px 18px 18px;
  }
  .product-pair__bottle--her {
    background: linear-gradient(180deg, var(--her-deep) 0%, var(--her-deep) 14%, var(--clear) 14%, var(--her-tone) 55%, var(--clear) 100%);
  }
  .product-pair__bottle--him {
    background: linear-gradient(180deg, var(--him-deep) 0%, var(--him-deep) 14%, var(--clear) 14%, var(--him-tone) 55%, var(--clear) 100%);
  }
  .headline {
    position: absolute;
    left: 0; right: 0; top: 1078px;
    text-align: center;
    font-size: 90px;
    font-weight: 400;
    letter-spacing: 0.18em;
    text-indent: 0.18em;
    line-height: 1;
    white-space: nowrap;
  }
</style>
</head>
<body>
  <main class="poster">
    <p class="tagline tagline--her">orba it for her</p>
    <p class="tagline tagline--him">orba it for him</p>

    <div class="product-pair" role="img" aria-label="Photograph of two interlocking clear bottles: a red-capped bottle with a pink ornamental label for her, and a blue-capped bottle with a light blue ornamental label for him">
      <div class="product-pair__bottle product-pair__bottle--her"></div>
      <div class="product-pair__bottle product-pair__bottle--him"></div>
    </div>

    <p class="tagline tagline--you">orba it for you</p>
    <h1 class="headline">LET’S ORBA</h1>
  </main>
</body>
</html>
```